Postcard flyers for text vouchers

Postcard flyer to drive people to text for local vouchers delivered straight to their mobile, alternatively they can check out the websites.
Double sided, full colour A6 size. 105mm x 148.5mm http://www.brintafold.com/supplying-artwork.html
Postcard will be available in high footfall areas must be eye catching and compelling, but keep message simple. Wording as attached, side one headline grabbing, side two in style of a tag cloud giving a flavour of vouchers/savings available in their local area.
Updates

Project Deadline Extended
Reason: Research has shown wider area for website required therefore by county [Kelmarsh Deals] rather than smaller regions. Focus on entertainment and shopping for flyer.

Target Market(s)

Target 18-55 year olds
Core 25-45???
male and female

Requirements
Must have
• Stand out

```html
<!DOCTYPE html>
<html lang="en">
<head>
<meta charset="utf-8">
<title>Vouchers Postcard Flyer</title>
<link rel="stylesheet" href="https://fonts.googleapis.com/css2?family=Archivo+Black&family=Arimo:wght@700&display=swap">
<style>
  :root {
    --paper: #ffffff;
    --card-dark: #231f20;
    --card-deep: #0f0d0d;
    --band-top: #ffd600;
    --band-mid: #fbb800;
    --band-bottom: #f39200;
    --tag-red: #e8423f;
    --tag-text: #e6e7f0;
    --ink: #000000;
    --light-text: #ffffff;
  }
  * { margin: 0; padding: 0; box-sizing: border-box; }
  html, body {
    width: 850px;
    height: 1200px;
    overflow: hidden;
    background: var(--paper);
  }
  .flyer {
    position: relative;
    width: 850px;
    height: 1200px;
    background: var(--paper);
    font-family: "Arimo", Arial, sans-serif;
  }
  .card {
    position: absolute;
    left: 33px;
    top: 35px;
    width: 784px;
    height: 1130px;
    border-radius: 28px;
    overflow: hidden;
    background: radial-gradient(ellipse at 55% 45%, #2e2a2b 0%, var(--card-dark) 55%, var(--card-deep) 100%);
  }
  .headline-band {
    position: absolute;
    left: 0;
    top: 42px;
    width: 100%;
    height: 333px;
    background: linear-gradient(180deg, var(--band-top) 0%, var(--band-mid) 50%, var(--band-bottom) 100%);
  }
  .tag {
    position: absolute;
    left: 0;
    top: 80px;
    width: 306px;
    height: 86px;
    background: var(--tag-red);
    transform: rotate(-3deg);
    transform-origin: left top;
    box-shadow: 3px 4px 8px rgba(0,0,0,0.35);
    z-index: 3;
  }
  .tag::after {
    content: "";
    position: absolute;
    inset: 5px;
    border: 2px dotted var(--tag-text);
  }
  .tag-label {
    position: absolute;
    left: 0;
    right: 0;
    top: 8px;
    text-align: center;
    font-family: "Arimo", Arial, sans-serif;
    font-weight: 700;
    font-size: 62px;
    letter-spacing: -1px;
    color: var(--tag-text);
    line-height: 1;
  }
  .offer {
    position: absolute;
    font-family: "Archivo Black", "Arial Black", sans-serif;
    color: var(--ink);
    line-height: 1;
    letter-spacing: -3px;
    z-index: 2;
  }
  .offer-two-for-one { left: 92px; top: 177px; font-size: 114px; }
  .offer-half-price { left: 256px; top: 288px; font-size: 114px; }
  .deal-list {
    position: absolute;
    left: 85px;
    top: 516px;
    list-style: none;
    color: var(--light-text);
    font-weight: 700;
    font-size: 25px;
    line-height: 34.3px;
  }
  .call-to-action {
    position: absolute;
    left: 33px;
    width: 784px;
    top: 985px;
    text-align: center;
    color: var(--light-text);
    font-weight: 700;
    font-size: 20.5px;
    line-height: 27.4px;
    padding-right: 0;
  }
</style>
</head>
<body>
  <main class="flyer">
    <section class="card">
      <div class="headline-band" role="img" aria-label="Orange and yellow band with decorative swirl pattern"></div>
      <div class="card-pattern" role="img" aria-label="Dark background with decorative swirl pattern"></div>
    </section>

    <div class="tag"><span class="tag-label">Vouchers</span></div>
    <h1 class="offer offer-two-for-one">2 for 1</h1>
    <p class="offer offer-half-price">50% Off</p>

    <ul class="deal-list">
      <li>Eating out</li>
      <li>Entertainment</li>
      <li>building/plumbing/home services huge discounts</li>
      <li>Free Entry for Events</li>
      <li>Theatre Deals</li>
      <li>Furniture&nbsp; vouchers</li>
      <li>Fashion Deals</li>
      <li>FREE sessions solicitors/accountants</li>
      <li>Insurance offers</li>
    </ul>

    <p class="call-to-action">
      Entertainment | Shopping | All Services<br>
      In<br>
      Malvern | Worcester | Hereford<br>
      Text for your free vouchers now! See over
    </p>
  </main>
</body>
</html>
```